Swerve (nightclub flyer)

Nightclub flyer, guaranteed project. Text below (and please use logos, large):

SWERVE PRESENTS:

KORVEN (LOGO) B2B MARTY DELANO (LOGO)

+TOBBI RASK (smaller text)

10/26/17

2284 ELM LANE SACRAMENTO CA
21+ 10PM-2AM

HOUSE/TECHNO

A VELVET ORCHID ENTERTAINMENT (LOGO) PRODUCTION

Target Market(s)

House/Electronic Music Lovers

Industry/Entity Type

Night Club

Font styles to use
Sans Serif

Colors

Designer to choose colors to be used in the design.

Requirements
Must have
• Large logos for the dj names, or large block letter dj names (logos not necessary if it looks better without. But KORVEN b2b MARTY DELANO large and TOBBI RASK smaller on separate line
Nice to have
• Can include a classy female model but nothing cheesy or too sexy

```html
<!DOCTYPE html>
<html lang="en">
<head>
<meta charset="utf-8">
<title>Swerve Presents – Nightclub Flyer</title>
<link rel="stylesheet" href="https://fonts.googleapis.com/css2?family=Fredoka:wght@600;700&family=Open+Sans:wght@400;600;700;800&display=swap">
<style>
  :root {
    --page-bg: #e4e2e6;
    --panel-top: #2b2b2b;
    --panel-bottom: #3a3a3a;
    --gold-light: #fff6b0;
    --gold-mid: #e8c95a;
    --gold-deep: #b58a1c;
    --white: #ffffff;
    --soft-white: #e6e6e6;
    --muted: #b9b9b9;
    --accent-blue: #1a9ee6;
    --ink: #1f1f1f;
    --rule: #8d8d8d;
  }
  * { margin: 0; padding: 0; box-sizing: border-box; }
  html, body {
    width: 1041px;
    height: 1200px;
    overflow: hidden;
    background: var(--page-bg);
  }
  .flyer {
    position: absolute;
    left: 93px;
    top: 0;
    width: 855px;
    height: 1200px;
    overflow: hidden;
    font-family: "Open Sans", sans-serif;
    color: var(--white);
    background: linear-gradient(180deg, var(--panel-top), var(--panel-bottom));
  }
  .hero-photo {
    position: absolute;
    left: 0; top: 0;
    width: 855px; height: 640px;
    background:
      radial-gradient(circle at 82% 28%, rgba(255,240,200,0.85) 0, rgba(255,200,120,0.35) 9%, transparent 22%),
      radial-gradient(circle at 30% 8%, rgba(255,235,190,0.7) 0, transparent 14%),
      radial-gradient(ellipse at 55% 55%, #8a5a34 0, #5a3419 45%, #2c180b 100%);
  }
  .headline {
    position: absolute;
    left: 0; width: 855px;
    top: 660px;
    text-align: center;
    font-family: "Fredoka", sans-serif;
    font-weight: 700;
    font-size: 72px;
    line-height: 1;
    letter-spacing: -1px;
    background: linear-gradient(180deg, var(--gold-light) 0%, var(--gold-mid) 50%, var(--gold-deep) 100%);
    -webkit-background-clip: text;
    background-clip: text;
    color: transparent;
  }
  .headline-rule {
    position: absolute;
    left: 80px; top: 740px;
    width: 695px; height: 3px;
    background: linear-gradient(90deg, transparent, var(--gold-mid) 50%, transparent);
  }
  .artists {
    position: absolute;
    left: 0; width: 855px;
    top: 764px; height: 64px;
    display: flex;
    align-items: center;
    justify-content: center;
    gap: 16px;
  }
  .artist-name {
    font-weight: 800;
    font-size: 50px;
    line-height: 1;
    letter-spacing: 1px;
    color: var(--white);
  }
  .artist-mark {
    display: flex;
    align-items: center;
    gap: 12px;
  }
  .artist-mark .dot {
    width: 44px; height: 44px;
    border-radius: 50%;
    background: #111;
    border: 2px solid var(--accent-blue);
  }
  .b2b {
    font-weight: 600;
    font-size: 24px;
    letter-spacing: 2px;
    color: var(--accent-blue);
  }
  .support {
    position: absolute;
    left: 0; width: 855px;
    top: 846px; height: 50px;
    display: flex;
    align-items: center;
    justify-content: center;
    gap: 12px;
  }
  .support-name {
    font-family: "Fredoka", sans-serif;
    font-weight: 700;
    font-size: 40px;
    background: linear-gradient(180deg, var(--gold-light), var(--gold-mid) 55%, var(--gold-deep));
    -webkit-background-clip: text;
    background-clip: text;
    color: transparent;
  }
  .date-block {
    position: absolute;
    left: 267px; width: 321px;
    top: 908px; height: 69px;
    border-top: 1px solid var(--rule);
    border-bottom: 1px solid var(--rule);
    text-align: center;
    font-weight: 600;
    font-size: 64px;
    line-height: 67px;
    color: var(--white);
  }
  .hours {
    position: absolute;
    left: 0; width: 855px;
    top: 986px;
    text-align: center;
    font-weight: 700;
    font-size: 24px;
    line-height: 32px;
  }
  .hours .unit { color: var(--accent-blue); }
  .hours .genre { margin-left: 18px; letter-spacing: 2px; color: var(--soft-white); }
  .age {
    position: absolute;
    left: 0; width: 855px;
    top: 1016px;
    text-align: center;
    font-weight: 400;
    font-size: 28px;
    line-height: 50px;
    color: var(--soft-white);
  }
  .age .age-limit {
    font-weight: 700;
    font-size: 46px;
    color: var(--accent-blue);
    margin-left: 12px;
    vertical-align: -4px;
  }
  .production {
    position: absolute;
    left: 0; width: 855px;
    top: 1078px; height: 40px;
    display: flex;
    align-items: center;
    justify-content: center;
    gap: 10px;
    font-weight: 600;
    font-size: 18px;
    letter-spacing: 2px;
    color: var(--muted);
  }
  .production .mark {
    width: 14px; height: 14px;
    background: var(--accent-blue);
  }
  .address-band {
    position: absolute;
    left: 0; top: 1139px;
    width: 855px; height: 61px;
    background: var(--white);
    color: var(--ink);
    text-align: center;
    font-weight: 700;
    font-size: 32px;
    line-height: 61px;
    letter-spacing: 0.5px;
  }
</style>
</head>
<body>
  <main class="flyer">
    <div class="hero-photo" role="img" aria-label="Model in a sequined dress posing before a curtain of glittering beaded strands with warm stage lights and a mirror ball"></div>

    <h1 class="headline">SWERVE PRESENTS</h1>
    <div class="headline-rule"></div>

    <div class="artists">
      <span class="artist-name">KORVEN</span>
      <span class="b2b">B2B</span>
      <div class="artist-mark">
        <span class="dot"></span>
        <span class="artist-name">MARTY DELANO</span>
      </div>
    </div>

    <div class="support">
      <svg class="headphones" width="62" height="44" viewBox="0 0 62 44" aria-hidden="true">
        <path d="M8 30 V22 a23 20 0 0 1 46 0 V30" fill="none" stroke="#1a9ee6" stroke-width="4"/>
        <rect x="2" y="24" width="14" height="20" rx="6" fill="#ffffff"/>
        <rect x="46" y="24" width="14" height="20" rx="6" fill="#ffffff"/>
        <rect x="12" y="24" width="5" height="20" rx="2" fill="#1a9ee6"/>
        <rect x="45" y="24" width="5" height="20" rx="2" fill="#1a9ee6"/>
      </svg>
      <span class="support-name">+ TOBBI RASK</span>
    </div>

    <div class="date-block">10/26/17</div>

    <p class="hours">10<span class="unit">PM</span>-2<span class="unit">AM</span><span class="genre">HOUSE/TECHNO</span></p>
    <p class="age">FOR PEOPLE AGES:<span class="age-limit">21+</span></p>

    <p class="production">A<span class="mark"></span>VELVET ORCHID ENTERTAINMENT PRODUCTION</p>

    <footer class="address-band">2284 ELM LANE SACRAMENTO CA</footer>
  </main>
</body>
</html>
```